"Use it or Lose it" and "Brush on Over"

We are a dental office looking to connect with our patients through direct mail advertising. With the last 3 months of the year coming we would like to send out Post Cards to our patients letting them know they have 3 months left to "USE IT OR LOSE IT" when it comes to their dental insurance benefits.
So we are looking for a post card that has the "Use It or Lost it" theme along with our dental office logo, telephone number and address.

We are also looking for a post card that says "Brush On Over" to remind our patients that they are due for a dental cleaning and we would like for them to come over to our dental office for a well needed cleaning :).

```html
<!DOCTYPE html>
<html lang="en">
<head>
<meta charset="utf-8">
<title>Linden Dental Postcards</title>
<link href="https://fonts.googleapis.com/css2?family=Oswald:wght@600&family=Jost:wght@400;500;600&display=swap" rel="stylesheet">
<style>
  :root {
    --navy: #0f3f86;
    --navy-deep: #0b2f66;
    --royal: #1a57b0;
    --sky: #3f86cf;
    --ink: #17408a;
    --paper: #ffffff;
    --rule: #cfd3d8;
    --label: #9a9ea4;
  }
  * { margin: 0; padding: 0; box-sizing: border-box; }
  html, body { width: 1200px; height: 2596px; overflow: hidden; background: var(--paper); }
  body { position: relative; font-family: "Jost", sans-serif; color: var(--ink); }

  .side-label {
    position: absolute; left: 109px; width: 0; height: 0;
    font-size: 16px; letter-spacing: 5px; color: var(--label); white-space: nowrap;
  }
  .side-label span { position: absolute; transform: translate(-50%, -50%) rotate(-90deg); }

  .postcard {
    position: absolute; left: 160px; width: 871px; height: 622px;
    background: var(--paper); overflow: hidden;
    box-shadow: 0 22px 40px rgba(0, 0, 0, 0.22);
  }
  .postcard.one { top: 166px; }
  .postcard.two { top: 900px; }
  .postcard.back { top: 1638px; }

  .front-field {
    position: absolute; left: 0; top: 0; width: 871px; height: 489px;
    background: linear-gradient(180deg, var(--navy-deep) 0%, var(--royal) 100%);
  }
  .bubble { position: absolute; left: 66px; top: 70px; width: 420px; height: 265px; }
  .bubble svg { position: absolute; inset: 0; }
  .headline {
    position: absolute; left: 0; width: 369px; top: 0; height: 265px;
    display: flex; flex-direction: column; justify-content: center; align-items: center;
    font-family: "Oswald", sans-serif; font-weight: 600; color: var(--paper);
    text-transform: uppercase; line-height: 0.98; font-size: 100px;
  }
  .headline small { font-family: "Jost", sans-serif; font-weight: 500; font-size: 32px; margin-left: 8px; vertical-align: 6px; }
  .headline.brush { font-size: 96px; }
  .front-note {
    position: absolute; left: 66px; width: 420px; color: var(--paper);
    text-align: center; font-size: 22px; line-height: 1.3;
  }
  .one .front-note { top: 398px; }
  .two .front-note { top: 382px; }
  .artwork {
    position: absolute;
    background: linear-gradient(180deg, #ffffff 0%, #e3eefb 70%, var(--sky) 100%);
    border-radius: 26px 26px 0 0;
  }
  .one .artwork { left: 508px; top: 32px; width: 300px; height: 457px; border-radius: 110px 110px 0 0; }
  .two .artwork { left: 508px; top: 78px; width: 272px; height: 411px; opacity: 0.9; }

  .contact-bar {
    position: absolute; left: 0; bottom: 0; width: 871px; height: 131px; background: var(--paper);
  }
  .back .contact-bar { border-top: 6px solid var(--navy-deep); height: 135px; }
  .brand {
    position: absolute; left: 62px; top: 42px; display: flex; align-items: center; gap: 14px;
    font-family: "Jost", sans-serif; font-weight: 500; font-size: 40px; letter-spacing: 1px;
    color: var(--ink); text-transform: uppercase;
  }
  .brand i { display: block; width: 36px; height: 36px; border-radius: 50%; background: var(--ink); }
  .contacts { position: absolute; top: 26px; font-size: 13px; line-height: 1.25; color: var(--ink); list-style: none; }
  .contacts.left { left: 448px; }
  .contacts.right { left: 643px; }
  .contacts li { display: flex; align-items: flex-start; gap: 10px; height: 30px; }
  .contacts svg { flex: none; width: 18px; height: 18px; margin-top: -2px; }

  .services-panel {
    position: absolute; left: 0; top: 0; width: 438px; height: 487px;
    background: linear-gradient(180deg, var(--navy-deep) 0%, var(--navy) 100%);
    color: var(--paper); text-align: center;
  }
  .services-title {
    position: absolute; left: 38px; top: 34px; width: 366px; height: 58px; background: var(--paper);
    border-radius: 4px; display: flex; align-items: center; justify-content: center;
    font-family: "Oswald", sans-serif; font-weight: 600; font-size: 24px; color: var(--ink);
    text-transform: uppercase;
  }
  .services-copy { position: absolute; left: 46px; top: 114px; width: 346px; font-size: 11.5px; line-height: 1.55; }
  .services-copy p + p { margin-top: 14px; }
  .services-list {
    position: absolute; left: 40px; top: 322px; width: 358px; list-style: none;
    display: grid; grid-template-columns: 1fr 1fr; column-gap: 12px; row-gap: 1px;
    font-size: 10px; font-weight: 600; text-transform: uppercase; line-height: 1.6;
  }
  .stamp-box { position: absolute; left: 743px; top: 23px; width: 94px; height: 104px; border: 3px solid var(--rule); border-radius: 6px; }
  .address-lines { position: absolute; left: 466px; top: 171px; width: 371px; }
  .address-lines hr { border: none; border-top: 2px solid var(--rule); margin-bottom: 45.6px; }
</style>
</head>
<body>

  <div class="side-label" style="top:404px"><span>POSTCARD 1</span></div>
  <div class="side-label" style="top:1140px"><span>POSTCARD 2</span></div>
  <div class="side-label" style="top:1948px"><span>BACK</span></div>

  <svg width="0" height="0" style="position:absolute">
    <defs>
      <symbol id="icon-phone" viewBox="0 0 20 20"><circle cx="10" cy="10" r="10" fill="#17408a"/><path d="M7 5.5l2 2-1 1.3c.6 1.3 1.6 2.3 2.9 2.9l1.3-1 2 2-1.2 1.4c-3.6-.5-6.8-3.7-7.3-7.3z" fill="#fff"/></symbol>
      <symbol id="icon-pin" viewBox="0 0 20 20"><circle cx="10" cy="10" r="10" fill="#17408a"/><path d="M10 4.5a3.6 3.6 0 0 0-3.6 3.6c0 2.7 3.6 7 3.6 7s3.6-4.3 3.6-7A3.6 3.6 0 0 0 10 4.5zm0 5a1.4 1.4 0 1 1 0-2.8 1.4 1.4 0 0 1 0 2.8z" fill="#fff"/></symbol>
      <symbol id="icon-fax" viewBox="0 0 20 20"><circle cx="10" cy="10" r="10" fill="#17408a"/><rect x="6" y="8" width="8" height="6" rx="1" fill="#fff"/><rect x="7.5" y="5" width="5" height="3" fill="#fff"/></symbol>
      <symbol id="icon-mail" viewBox="0 0 20 20"><circle cx="10" cy="10" r="10" fill="#17408a"/><rect x="5.5" y="6.5" width="9" height="7" rx="1" fill="#fff"/><path d="M5.8 7l4.2 3.3L14.2 7" stroke="#17408a" stroke-width="1" fill="none"/></symbol>
      <symbol id="icon-web" viewBox="0 0 20 20"><circle cx="10" cy="10" r="10" fill="#17408a"/><circle cx="10" cy="10" r="4.5" fill="none" stroke="#fff" stroke-width="1.3"/><path d="M5.5 10h9M10 5.5c-2 2.5-2 6.5 0 9M10 5.5c2 2.5 2 6.5 0 9" stroke="#fff" stroke-width="1" fill="none"/></symbol>
    </defs>
  </svg>

  <!-- Postcard 1 -->
  <section class="postcard one">
    <div class="front-field">
      <div class="bubble">
        <svg width="420" height="265" viewBox="0 0 420 265"><path d="M18 0h333a18 18 0 0 1 18 18v104l40 24-40 24v77a18 18 0 0 1-18 18H18A18 18 0 0 1 0 247V18A18 18 0 0 1 18 0z" fill="#3f86cf"/></svg>
        <h1 class="headline"><span>Use it<small>or</small></span><span>Lose it</span></h1>
      </div>
      <p class="front-note">Use your dental insurance benefits<br>before December 31st or you lose them!</p>
      <div class="artwork" role="img" aria-label="Smiling cartoon tooth illustration"></div>
    </div>
    <footer class="contact-bar">
      <div class="brand"><i></i>Linden Dental</div>
      <ul class="contacts left">
        <li><svg><use href="#icon-phone"/></svg>555 - 014 - 1717</li>
        <li><svg><use href="#icon-pin"/></svg>28 Orchard Lane<br>Brookvale, NJ 07999</li>
      </ul>
      <ul class="contacts right">
        <li><svg><use href="#icon-fax"/></svg>555 - 014 - 1793</li>
        <li><svg><use href="#icon-mail"/></svg>lindendental@mailbox.example</li>
        <li><svg><use href="#icon-web"/></svg>LindenDental.example</li>
      </ul>
    </footer>
  </section>

  <!-- Postcard 2 -->
  <section class="postcard two">
    <div class="front-field">
      <div class="bubble">
        <svg width="420" height="265" viewBox="0 0 420 265"><path d="M18 0h333a18 18 0 0 1 18 18v104l40 24-40 24v77a18 18 0 0 1-18 18H18A18 18 0 0 1 0 247V18A18 18 0 0 1 18 0z" fill="#3f86cf"/></svg>
        <h1 class="headline brush"><span>Brush</span><span>On Over</span></h1>
      </div>
      <p class="front-note">You are due to a dental cleaning.<br>Come over to our dental clinic<br>for a well needed cleaning.</p>
      <div class="artwork" role="img" aria-label="Line illustration of a smiling dental mirror and a dental probe"></div>
    </div>
    <footer class="contact-bar">
      <div class="brand"><i></i>Linden Dental</div>
      <ul class="contacts left">
        <li><svg><use href="#icon-phone"/></svg>555 - 014 - 1717</li>
        <li><svg><use href="#icon-pin"/></svg>28 Orchard Lane<br>Brookvale, NJ 07999</li>
      </ul>
      <ul class="contacts right">
        <li><svg><use href="#icon-fax"/></svg>555 - 014 - 1793</li>
        <li><svg><use href="#icon-mail"/></svg>lindendental@mailbox.example</li>
        <li><svg><use href="#icon-web"/></svg>LindenDental.example</li>
      </ul>
    </footer>
  </section>

  <!-- Back -->
  <section class="postcard back">
    <div class="services-panel">
      <h2 class="services-title">Our Dental Services</h2>
      <div class="services-copy">
        <p>Your dental health is important, and to ensure that you have a healthy, beautiful smile throughout your entire life, you need to practice good oral hygiene for life. But sometimes, good dental habits themselves aren't enough to keep you smiling beautifully. Sometimes, you need a little help from an expert dentist.</p>
        <p>The experienced team at Linden Dental is just the expert for you! With over fifty years' experience in the business, we have all the skills and know-how to ensure that you maintain the most beautiful smile possible! We can do so with our top-of-the-line dental services, which include the following:</p>
      </div>
      <ul class="services-list">
        <li>Preventive Dentistry</li><li>Tooth-Colored Fillings</li>
        <li>Checkups &amp; Cleanings</li><li>Clear Aligners</li>
        <li>Digital X-Rays</li><li>Porcelain Veneers</li>
        <li>Restorative Dentistry</li><li>All-Ceramic Restorations</li>
        <li>Crowns &amp; Bridges</li><li>Pediatric Dentistry</li>
        <li>Dental Implants</li><li>Emergency Care</li>
        <li>Cosmetic Dentistry</li><li>Sleep Apnea Therapy</li>
      </ul>
    </div>
    <div class="stamp-box"></div>
    <div class="address-lines"><hr><hr><hr><hr><hr><hr></div>
    <footer class="contact-bar">
      <div class="brand"><i></i>Linden Dental</div>
      <ul class="contacts left">
        <li><svg><use href="#icon-phone"/></svg>555 - 014 - 1717</li>
        <li><svg><use href="#icon-pin"/></svg>28 Orchard Lane<br>Brookvale, NJ 07999</li>
      </ul>
      <ul class="contacts right">
        <li><svg><use href="#icon-fax"/></svg>555 - 014 - 1793</li>
        <li><svg><use href="#icon-mail"/></svg>lindendental@mailbox.example</li>
        <li><svg><use href="#icon-web"/></svg>LindenDental.example</li>
      </ul>
    </footer>
  </section>

</body>
</html>
```